New company documents design

Hi Kip,
We are looking for new versions of the below and would like these all be the in the same theme / style. The product data sheets with the company logo in the top left and the footer with the green highting over the website works well. Can this style be applied to the below:
- Business cards, w/QR code function
- Blank Letter Head
- Blank power point
- Blank Document (example attached, WHS-FRM)
- Email signature
- Corporate profile (copy attached)

```html
<!DOCTYPE html>
<html lang="en">
<head>
<meta charset="utf-8">
<title>Ridgeline Engineering – Letterhead</title>
<link rel="stylesheet" href="https://fonts.googleapis.com/css2?family=Arimo:wght@400&family=Montserrat:wght@700&family=Roboto:wght@400&display=swap">
<style>
  :root {
    --backdrop: #dcdcdc;
    --paper: #f8f8f8;
    --brand-blue: #1f3c8f;
    --brand-green: #17964a;
    --ink: #2a2a2a;
    --footer-ink: #666666;
    --white: #ffffff;
  }
  * { box-sizing: border-box; margin: 0; padding: 0; }
  html, body {
    width: 1153px; height: 1200px; overflow: hidden;
    background: var(--backdrop);
  }
  .letterhead {
    position: absolute; left: 160px; top: 20px;
    width: 832px; height: 1160px;
    background: var(--paper);
    font-family: "Arimo", Arial, sans-serif;
    color: var(--ink);
    overflow: hidden;
  }
  .top-rule {
    position: absolute; left: 0; top: 0; width: 100%; height: 6px;
    background: var(--brand-blue);
  }
  .top-rule-accent {
    position: absolute; right: 0; top: 6px; width: 160px; height: 3px;
    background: var(--brand-green);
  }
  .brand {
    position: absolute; left: 101px; top: 66px;
    display: flex; align-items: center; gap: 14px;
  }
  .brand-mark { width: 22px; height: 22px; background: var(--brand-blue); }
  .brand-name {
    font-family: "Montserrat", Arial, sans-serif; font-weight: 700;
    font-size: 26px; line-height: 1.15; color: var(--brand-blue);
    text-transform: uppercase; letter-spacing: 0.5px;
  }
  .text-block {
    position: absolute; left: 101px; width: 640px;
    font-size: 13.2px; line-height: 17.8px; letter-spacing: -0.15px;
  }
  .recipient { top: 309px; font-style: normal; }
  .salutation { top: 469px; }
  .body-copy { top: 505px; text-align: justify; hyphens: auto; -webkit-hyphens: auto; }
  .body-copy p + p { margin-top: 17.8px; }
  .closing { top: 775px; }
  .signature-area {
    position: absolute; left: 101px; top: 803px;
    width: 188px; height: 64px;
    background: linear-gradient(90deg, #ececec, #f4f4f4);
    border-radius: 4px;
  }
  .signatory { top: 899px; }
  .contact-line {
    position: absolute; left: 101px; width: 640px; top: 1104px;
    display: flex; justify-content: space-between; align-items: center;
    font-family: "Roboto", Arial, sans-serif;
    font-size: 14px; color: var(--footer-ink); letter-spacing: 0.6px;
  }
  .contact-item { display: flex; align-items: center; gap: 5px; }
  .footer-band {
    position: absolute; left: 0; bottom: 0; width: 100%; height: 28px;
    background: var(--brand-green); color: var(--white);
    display: flex; justify-content: center; align-items: center; gap: 6px;
    font-family: "Roboto", Arial, sans-serif;
    font-size: 14px; letter-spacing: 0.6px;
  }
</style>
</head>
<body>
  <main class="letterhead">
    <div class="top-rule"></div>
    <div class="top-rule-accent"></div>

    <header class="brand">
      <span class="brand-mark"></span>
      <span class="brand-name">Ridgeline<br>Engineering</span>
    </header>

    <address class="text-block recipient">
      First Name Last Name<br>
      Addressee’s name<br>
      Building number/name and street<br>
      Post Town, Post Code
    </address>

    <p class="text-block salutation">Dear First Name</p>

    <section class="text-block body-copy">
      <p>Lorem ipsum dolor sit amet, consectetur adipiscing elit. Vestibulum eu vulputate sapien. In quis imperdiet lectus, eget accumsan sem. Vestibulum consequat rhoncus cursus. Quisque ultrices facilisis libero, eu facilisis nisl congue sit amet. Phasellus consequat justo mi. In sollicitudin justo sed eros blandit, non eleifend elit fauci&shy;bus. Aliquam elit purus, facilisis at pulvinar eu, rutrum ut mauris. Suspendisse aliquam ipsum vitae egestas venenatis. Quisque a lacinia orci, sit amet tincidunt diam. Nulla blandit justo sit amet purus gravida, pulvinar iaculis sapien egestas. Sed vehicula diam leo, et vehicula leo elementum et. Duis nec suscipit justo. Maecenas eget pretium leo. Quisque imperdiet ut quam ut placerat. Duis facilisis, nisi sit amet dictum egestas, neque nulla elementum nibh, in ultrices mi magna nec metus.</p>
      <p>Duis arcu lacus, accumsan id lectus eu, condimentum tincidunt purus. Cras ac justo sed odio mattis gravida consectetur ac sapien. Integer eleifend enim et ipsum fermentum auctor. Quisque at porttitor velit. Aenean gravida nibh odio, eget tempus mauris semper at. In consectetur sed leo ut molestie. Sed pharetra urna quis turpis fringilla, ut posuere massa hendrerit. Proin pulvinar nibh augue, vel luctus elit aliquet non. Nunc elemen&shy;tum iaculis turpis eu interdum. Pellentesque non imperdiet magna, ut facilisis augue.</p>
    </section>

    <p class="text-block closing">Sincerely,</p>

    <div class="signature-area" role="img" aria-label="Handwritten signature of the sender"></div>

    <p class="text-block signatory">First Name Last Name<br>Position</p>

    <footer>
      <div class="contact-line">
        <span class="contact-item">
          <svg width="14" height="14" viewBox="0 0 24 24" aria-hidden="true"><path fill="var(--brand-green)" d="M6.6 10.8a15.1 15.1 0 0 0 6.6 6.6l2.2-2.2c.3-.3.7-.4 1-.2 1.1.4 2.3.6 3.6.6.6 0 1 .4 1 1V20c0 .6-.4 1-1 1A17 17 0 0 1 3 4c0-.6.4-1 1-1h3.5c.6 0 1 .4 1 1 0 1.3.2 2.5.6 3.6.1.3 0 .7-.2 1z"/></svg>
          +61 (0) 8 5550 2184
        </span>
        <span class="contact-item">
          <svg width="12" height="16" viewBox="0 0 24 32" aria-hidden="true"><path fill="var(--brand-green)" d="M12 0A11 11 0 0 0 1 11c0 8 11 21 11 21s11-13 11-21A11 11 0 0 0 12 0zm0 15a4 4 0 1 1 0-8 4 4 0 0 1 0 8z"/></svg>
          48 Calder St, Westbrook 6100
        </span>
        <span class="contact-item">
          <svg width="16" height="12" viewBox="0 0 24 18" aria-hidden="true"><rect x="1" y="1" width="22" height="16" fill="none" stroke="var(--brand-green)" stroke-width="2"/><path d="M1 1l11 9 11-9M1 17l8-7M23 17l-8-7" fill="none" stroke="var(--brand-green)" stroke-width="2"/></svg>
          info@ridgelineeng.com.au
        </span>
      </div>
      <div class="footer-band">
        <svg width="13" height="13" viewBox="0 0 24 24" aria-hidden="true"><g fill="none" stroke="var(--white)" stroke-width="1.8"><circle cx="12" cy="12" r="10"/><ellipse cx="12" cy="12" rx="4.5" ry="10"/><path d="M2 12h20M4 6.5h16M4 17.5h16"/></g></svg>
        www.ridgelineeng.com.au
      </div>
    </footer>
  </main>
</body>
</html>
```